Business Card Design

Certified GKL Instructor. Self defense instruction. Ladies classes available. Semi automatic and revolver

Industry/Entity Type

Defense

```html
<!DOCTYPE html>
<html lang="en">
<head>
<meta charset="UTF-8">
<title>GKL Instructor Business Card</title>
<link rel="stylesheet" href="https://fonts.googleapis.com/css2?family=Stardos+Stencil:wght@700&family=Alegreya:ital@1&display=swap">
<style>
  :root {
    --page: #ffffff;
    --parchment-light: #e6d3a4;
    --parchment-mid: #d2b47a;
    --parchment-dark: #8f6d3c;
    --ink: #1c140c;
    --ink-soft: #2e261d;
    --seal-blue: #1f3d9a;
    --seal-ring: #ffffff;
  }
  * { margin: 0; padding: 0; box-sizing: border-box; }
  html, body {
    width: 1200px;
    height: 702px;
    overflow: hidden;
    background: var(--page);
  }
  .card {
    position: absolute;
    left: 20px;
    top: 20px;
    width: 1158px;
    height: 662px;
    overflow: hidden;
  }
  .card__backdrop {
    position: absolute;
    inset: 0;
    background:
      radial-gradient(ellipse 55% 60% at 22% 38%, rgba(169,162,145,0.55), rgba(169,162,145,0) 70%),
      radial-gradient(ellipse 70% 65% at 55% 45%, var(--parchment-light), var(--parchment-mid) 70%, var(--parchment-dark) 110%);
  }
  .quote {
    position: absolute;
    left: 0;
    width: 1158px;
    top: 58px;
    text-align: center;
    white-space: nowrap;
    text-transform: uppercase;
    font-family: "Stardos Stencil", "Courier New", monospace;
    font-weight: 700;
    font-size: 28px;
    line-height: 40px;
    letter-spacing: 0.3px;
    color: var(--ink);
  }
  .services {
    position: absolute;
    left: 0;
    width: 1158px;
    text-align: center;
    white-space: nowrap;
    font-family: "Alegreya", Georgia, serif;
    font-style: italic;
    font-size: 33px;
    letter-spacing: 0.6px;
    color: var(--ink-soft);
  }
  .services--defense { top: 255px; line-height: 44px; }
  .services--firearms { top: 389px; line-height: 44px; }
  .contact {
    position: absolute;
    left: 72px;
    top: 529px;
    white-space: nowrap;
    font-family: "Alegreya", Georgia, serif;
    font-style: italic;
    font-size: 32px;
    line-height: 44px;
    letter-spacing: 0.3px;
    color: var(--ink-soft);
  }
  .seal {
    position: absolute;
    left: 519px;
    top: 513px;
  }
  .instructor {
    position: absolute;
    left: 719px;
    width: 420px;
    top: 494px;
    text-align: center;
    white-space: nowrap;
  }
  .instructor__name {
    font-family: "Stardos Stencil", "Courier New", monospace;
    font-weight: 700;
    font-size: 52px;
    line-height: 58px;
    letter-spacing: 0.5px;
    color: var(--ink);
  }
  .instructor__title {
    margin-top: 8px;
    font-family: "Alegreya", Georgia, serif;
    font-style: italic;
    font-size: 31px;
    letter-spacing: 0.3px;
    color: var(--ink-soft);
  }
</style>
</head>
<body>
  <div class="card">
    <div class="card__backdrop" role="img" aria-label="Aged parchment collage of a waving stars-and-stripes flag over a handwritten constitution document"></div>

    <p class="quote">"A well regulated militia, being necessary to the security of a<br>free state, the right of the people to keep and bear arms,<br>shall not be infringed."</p>

    <p class="services services--defense">Self-Defense Instruction<br>Ladies Classes Available!</p>
    <p class="services services--firearms">Semi-Automatic &amp; Revolver Classes</p>

    <p class="contact">Phone: (555)-555-0142<br>Email: M.ellison@postmail.com</p>

    <svg class="seal" width="122" height="122" viewBox="0 0 122 122" aria-hidden="true">
      <circle cx="61" cy="61" r="60" fill="var(--seal-blue)"/>
      <circle cx="61" cy="61" r="40" fill="var(--seal-ring)"/>
    </svg>

    <div class="instructor">
      <p class="instructor__name">MARK ELLISON</p>
      <p class="instructor__title">Certified GKL Instructor</p>
    </div>
  </div>
</body>
</html>
```